Ledger Tide Pro Banner Ad campaign

We are the number 1 leading automated journal & analytics platform for active traders in the crypto space

We will be running banner ads on a specialist ad network and need HTML designs + a good strategy.

Some of our key selling points to consider including:

- The #1 automated journaling & analytics solution for Crypto Traders
- We save traders time (from manual data entry that can be automated by our journal trade import service)
- We help traders improve through detailed analytics feedback on their trading performance
- LTP has helped thousands of crypto traders improve performance
- 5,700+ traders are using LTP to save themselves hundreds of data entry hours per year
- Analyse your full trade history in a click!

I have attached an example mockup we came up with internally but we are not professionals. Use it as a guide to heavily improve upon in the context of general design quality, and 'sales-y' lingo to improve conversions

Have added a £100 1st place payment increase upon advice from a designer Should incentivise the best of the best to submit work

Target Market(s)

Active traders in the crypto derivatives space. Trading on the following exchanges:

- Travora.com
- Quellix.com
- Morvane.com
- ZQK.com

Font styles to use
Other font styles liked:
• Quicksand is our main font atm

Colors
3277b5
33a6d7
0792cd
85abd2
3276b5
85acd3
85cae6
86cae7

Requirements
Must have
• similar colour scheme from my example upload.

Check our main website for more: ledgertidepro.com

Although bare in mind, its a bit old and shitty. We are now working with specialists to improve, so feel free to have some creative freedom
Nice to have
• Nice clear custom icons to accompany text. And a rotation of 2 or 3 of the main selling points from the project description

```html
<!DOCTYPE html>
<html lang="en">
<head>
<meta charset="utf-8">
<title>Ledger Tide Pro — Banner Ad Set</title>
<link href="https://fonts.googleapis.com/css2?family=Quicksand:wght@400;500&family=Rubik:wght@500;700&family=Poppins:wght@500&display=swap" rel="stylesheet">
<style>
  :root{
    --canvas:#ffffff;
    --navy:#0a1c2a;
    --navy-edge:#1d3b52;
    --brand-blue:#3277b5;
    --brand-sky:#33a6d7;
    --brand-cyan:#33c1f0;
    --brand-soft:#85abd2;
    --brand-pale:#86cae7;
    --panel:#f3f4f5;
    --ink:#111418;
    --cta:#f7ec13;
    --headline-yellow:#f4e61c;
    --white:#ffffff;
  }
  *{margin:0;padding:0;box-sizing:border-box}
  html,body{width:1200px;height:1039px;overflow:hidden;background:var(--canvas)}
  .sheet{position:relative;width:1200px;height:1039px}
  .banner{position:absolute;width:529px;height:277px;overflow:hidden}
  .b1{left:49px;top:57px}
  .b2{left:622px;top:57px}
  .b3{left:49px;top:381px}
  .b4{left:622px;top:381px}
  .b5{left:49px;top:705px}
  .b6{left:622px;top:705px}
  .layer{position:absolute;inset:0}
  .photo{position:absolute}

  .brand{position:absolute;display:flex;flex-direction:column;align-items:center;gap:9px;
    font-family:"Quicksand",sans-serif;font-weight:400;font-size:12px;letter-spacing:1.6px;white-space:nowrap}
  .brand-mark{width:14px;height:14px;border:1px solid currentColor}
  .brand--center{left:50%;transform:translateX(-50%)}

  .headline{position:absolute;font-family:"Rubik",sans-serif;font-weight:700;text-transform:uppercase;white-space:nowrap}
  .subline{position:absolute;font-family:"Quicksand",sans-serif;font-weight:400;font-size:8px;line-height:14px;color:var(--white);opacity:.85}

  .cta{position:absolute;width:134px;height:22px;border-radius:11px;background:var(--cta);
    font-family:"Poppins",sans-serif;font-weight:500;font-size:7px;color:var(--ink);
    display:flex;align-items:center;justify-content:center}
</style>
</head>
<body>
<div class="sheet">

  <!-- Banner 1: the #1 solution -->
  <section class="banner b1">
    <svg class="layer" width="529" height="277" viewBox="0 0 529 277">
      <rect width="529" height="277" fill="var(--navy)"/>
      <polygon points="0,0 74,0 0,55" fill="var(--navy-edge)"/>
      <polygon points="455,0 529,0 529,55" fill="var(--navy-edge)"/>
      <polygon points="0,222 0,277 74,277" fill="var(--navy-edge)"/>
      <polygon points="529,222 529,277 455,277" fill="var(--navy-edge)"/>
    </svg>
    <div class="photo" role="img" aria-label="Glowing candlestick chart rising above an open hand"
      style="left:160px;top:66px;width:260px;height:211px;background:radial-gradient(ellipse at 50% 40%,rgba(51,166,215,.35),rgba(10,28,42,0) 70%)"></div>
    <div class="brand brand--center" style="top:15px;color:var(--white)"><span class="brand-mark"></span>LEDGER TIDE PRO</div>
    <h2 class="headline" style="left:0;width:529px;text-align:center;top:136px;font-size:15.5px;line-height:20px;color:var(--headline-yellow)">The #1 automated journaling &amp; analytics<br>solution for crypto traders</h2>
    <div class="cta" style="left:198px;top:178px">Start Your Free Trial Now</div>
  </section>

  <!-- Banner 2: save time -->
  <section class="banner b2">
    <div class="layer" style="background:linear-gradient(120deg,#2a64ad,#2f72bb 60%,#2a5fa6)"></div>
    <svg class="photo" role="img" aria-label="Businessman using a tablet in front of a warehouse" width="529" height="277" viewBox="0 0 529 277" style="left:0;top:0">
      <defs><linearGradient id="scene2" x1="0" y1="0" x2="1" y2="1"><stop offset="0" stop-color="#6a86a6"/><stop offset="1" stop-color="#1d3658"/></linearGradient></defs>
      <polygon points="0,215 529,64 529,277 0,277" fill="url(#scene2)"/>
    </svg>
    <div class="brand brand--center" style="top:15px;color:var(--white)"><span class="brand-mark"></span>LEDGER TIDE PRO</div>
    <h2 class="headline" style="left:57px;top:94px;font-size:17px;color:var(--brand-cyan)">We save traders time</h2>
    <p class="subline" style="left:57px;top:113px">from manual data entry that can be automated by our<br>journal trade import service</p>
    <div class="cta" style="left:57px;top:154px">Start Your Free Trial Now</div>
  </section>

  <!-- Banner 3: analytics feedback -->
  <section class="banner b3">
    <div class="photo" role="img" aria-label="Hands holding a phone in front of glowing market charts"
      style="left:0;top:0;width:410px;height:277px;background:linear-gradient(135deg,#3a2a4a,#c07a5a 55%,#2a1a22)"></div>
    <div class="layer" style="left:404px;background:var(--brand-blue)"></div>
    <svg class="layer" width="529" height="277" viewBox="0 0 529 277">
      <polygon points="249,34 529,3 529,272 249,245" fill="var(--panel)"/>
    </svg>
    <div class="brand" style="left:389px;transform:translateX(-50%);top:60px;color:#4a87c5"><span class="brand-mark"></span>LEDGER TIDE PRO</div>
    <h2 class="headline" style="left:249px;width:280px;text-align:center;top:134px;font-size:11.5px;line-height:15.5px;color:var(--ink)">We help traders improve<br>through detailed analytics feedback<br>on their trading performance</h2>
    <div class="cta" style="left:322px;top:199px">Start Your Free Trial Now</div>
  </section>

  <!-- Banner 4: thousands helped -->
  <section class="banner b4">
    <div class="photo" role="img" aria-label="Trader working on a laptop on a sunny beach"
      style="left:0;top:0;width:529px;height:277px;background:linear-gradient(180deg,#9fd0e0 0%,#cfe3e6 35%,#ecdcc4 60%,#e2c9a6 100%)"></div>
    <svg class="layer" width="529" height="277" viewBox="0 0 529 277">
      <rect x="265" y="25" width="70" height="70" transform="rotate(45 300 60)" fill="var(--brand-soft)" opacity=".35"/>
      <rect x="350" y="75" width="150" height="150" transform="rotate(45 425 150)" fill="var(--brand-soft)" opacity=".55"/>
      <rect x="160" y="40" width="80" height="80" transform="rotate(45 200 80)" fill="none" stroke="var(--white)" stroke-opacity=".5"/>
    </svg>
    <div class="brand" style="left:9px;top:6px;align-items:center;color:rgba(255,255,255,.85)"><span class="brand-mark"></span>LEDGER TIDE PRO</div>
    <h2 class="headline" style="left:6px;top:96px;font-size:11.5px;line-height:15.5px;color:var(--ink)">LTP has helped thousands of<br>crypto traders improve<br>performance</h2>
    <div class="cta" style="left:6px;top:155px">Start Your Free Trial Now</div>
  </section>

  <!-- Banner 5: 5,700+ traders -->
  <section class="banner b5">
    <div class="photo" role="img" aria-label="Hands holding a phone showing a rising price chart"
      style="left:150px;top:0;width:379px;height:277px;background:linear-gradient(135deg,#5a3a22,#b36a32 45%,#2a1a10)"></div>
    <svg class="layer" width="529" height="277" viewBox="0 0 529 277">
      <polygon points="177,0 200,0 290,138 200,277 177,277 267,138" fill="#1f3f6e"/>
      <polygon points="0,0 177,0 267,138 177,277 0,277" fill="var(--panel)"/>
    </svg>
    <div class="brand" style="left:9px;top:9px;color:#4a87c5"><span class="brand-mark"></span>LEDGER TIDE PRO</div>
    <h2 class="headline" style="left:18px;top:115px;font-size:11.5px;line-height:15.5px;color:var(--ink)">5,700+ traders are using LTP to<br>save themselves hundreds of data<br>entry hours per year</h2>
    <div class="cta" style="left:18px;top:174px">Start Your Free Trial Now</div>
  </section>

  <!-- Banner 6: full history in a click -->
  <section class="banner b6">
    <svg class="layer" width="529" height="277" viewBox="0 0 529 277">
      <defs>
        <linearGradient id="grid6" x1="0" y1="0" x2="0" y2="1"><stop offset="0" stop-color="#2b6fb2"/><stop offset="1" stop-color="#1d5596"/></linearGradient>
        <pattern id="gridlines" width="66" height="40" patternUnits="userSpaceOnUse"><path d="M66 0V40M0 40H66" stroke="var(--brand-sky)" stroke-opacity=".35" stroke-width="1" fill="none"/></pattern>
      </defs>
      <rect width="529" height="277" fill="url(#grid6)"/>
      <rect width="529" height="277" fill="url(#gridlines)"/>
      <polyline points="0,210 80,220 160,205 230,190 300,150 380,120 450,95 529,70" fill="none" stroke="var(--brand-pale)" stroke-opacity=".5"/>
    </svg>
    <div class="photo" role="img" aria-label="Illustrated trader meditating calmly in front of charts"
      style="left:250px;top:60px;width:200px;height:217px;border-radius:100px 100px 40px 40px;background:linear-gradient(180deg,#3a78b8,#2a5f9c)"></div>
    <div class="brand" style="left:22px;top:5px;color:var(--white)"><span class="brand-mark"></span>LEDGER TIDE PRO</div>
    <h2 class="headline" style="left:24px;top:103px;font-size:15px;line-height:19.5px;color:var(--headline-yellow)">Analyse your full trade<br>history in a click!</h2>
    <div class="cta" style="left:24px;top:148px">Start Your Free Trial Now</div>
  </section>

</div>
</body>
</html>
```